bottle label/ product label for smoothies (ultra fresh)

Please create a bottle label for our smoothies for retail distribution.
It's important that the following key features are clearly stated:

Ultra-fresh

Handmade

No preservatives

Not heat-treated

No added sugar

The base of the product label should be transparent, so that the color and content of the smoothie can be seen clearly.

We are a young, dynamic company. Our values are honesty, ultra-freshness, and authenticity — and we are the only ones producing this type of product in our country. We are positioned in the premium segment.

Design style: Modern, clean, and natural — but not playful or childish.

Example product: Selu Vane (Mango, Pineapple, Lemon, Passion Fruit, Orange)

Wenn du möchtest, kann ich auch gleich einen konkreten Vorschlag für das Etikettendesign auf Englisch oder einen Entwurfstext für das Label selbst erstellen. Sag einfach Bescheid!

Target Market(s)

trade - convenience

Industry/Entity Type

trade

Font styles to use
Sans Serif

Requirements
Must have
• sales- features: Ultra-fresh Handmade No preservatives Not heat-treated No added sugar

```html
<!DOCTYPE html>
<html lang="en">
<head>
<meta charset="utf-8">
<title>Navisa – Selu Vane smoothie label</title>
<link href="https://fonts.googleapis.com/css2?family=Bebas+Neue&family=Oswald:wght@300;500&family=Montserrat:wght@500;600&display=swap" rel="stylesheet">
<style>
  :root {
    --ink: #000000;
    --paper: #ffffff;
    --slate: #606060;
    --smoothie-light: #f0ae32;
    --smoothie-deep: #dc8a1c;
    --fruit-dark: #1a1a1a;
    --fruit-light: #f4f4f4;
  }
  * { margin: 0; padding: 0; box-sizing: border-box; }
  html, body { width: 712px; height: 1200px; overflow: hidden; background: var(--paper); }
  .sheet { position: relative; width: 712px; height: 1200px; }

  .label {
    position: absolute;
    width: 356px;
    height: 489px;
    color: var(--label-ink);
    background: var(--label-bg);
  }
  .label--light { left: 0; top: 0; --label-ink: var(--ink); --label-bg: var(--paper); --fruit: var(--fruit-dark); }
  .label--dark  { left: 356px; top: 0; --label-ink: var(--paper); --label-bg: var(--slate); --fruit: var(--fruit-light); }
  .label--clear { left: 178px; top: 600px; --label-ink: var(--paper); --label-bg: transparent; --fruit: rgba(255,255,255,0.35); }

  .smoothie-field {
    position: absolute; left: 0; top: 489px; width: 712px; height: 711px;
    background: radial-gradient(ellipse at 50% 45%, var(--smoothie-light), var(--smoothie-deep));
  }

  .brand-name {
    position: absolute; left: 0; right: 0; top: 36px;
    text-align: center;
    font-family: "Montserrat", sans-serif; font-weight: 600;
    font-size: 50px; letter-spacing: 0.5px; line-height: 1;
  }

  .divider {
    position: absolute; left: 97px; top: 110px; width: 2px; height: 309px;
    background: var(--label-ink);
  }

  .claims { position: absolute; left: 30px; top: 118px; width: 60px; list-style: none; }
  .claim {
    display: flex; flex-direction: column; align-items: center;
    font-family: "Montserrat", sans-serif; font-weight: 600;
    font-size: 5.6px; line-height: 1.25; text-align: center; letter-spacing: 0.2px;
    margin-bottom: 8px;
  }
  .claim svg { width: 38px; height: 38px; margin-bottom: 3px; color: var(--label-ink); }

  .product-name {
    position: absolute; left: 117px; top: 183px;
    font-family: "Bebas Neue", sans-serif; font-size: 36px; line-height: 1; letter-spacing: 0.3px;
  }
  .ingredients {
    position: absolute; left: 116px; top: 228px;
    font-family: "Oswald", sans-serif; font-weight: 300;
    font-size: 23px; line-height: 27px; text-transform: uppercase; letter-spacing: -0.6px;
  }
  .fruit-art {
    position: absolute; left: 210px; top: 300px; width: 110px; height: 106px;
    border-radius: 50% 50% 45% 45%;
    background: var(--fruit); opacity: 0.85;
  }
  .tagline {
    position: absolute; left: 0; right: 0; top: 432px; text-align: center;
    font-family: "Oswald", sans-serif; font-weight: 500;
    font-size: 10.5px; text-transform: uppercase; letter-spacing: -0.2px;
  }
</style>
</head>
<body>
<svg width="0" height="0" style="position:absolute" aria-hidden="true">
  <defs>
    <symbol id="icon-fresh" viewBox="0 0 40 40" fill="none" stroke="currentColor" stroke-width="1.4" stroke-linecap="round" stroke-linejoin="round">
      <ellipse cx="20" cy="33" rx="14" ry="3.5"/>
      <path d="M20 31 C12 26 12 15 20 8 C28 15 28 26 20 31Z"/>
      <path d="M20 31 V13 M20 18 L16 15 M20 23 L24 20 M20 27 L16 24"/>
      <path d="M6 7 l1 2 2 1 -2 1 -1 2 -1 -2 -2 -1 2 -1Z M33 10 l1 2 2 1 -2 1 -1 2 -1 -2 -2 -1 2 -1Z M5 19 l1 1.5 1.5 1 -1.5 1 -1 1.5 -1 -1.5 -1.5 -1 1.5 -1Z"/>
    </symbol>
    <symbol id="icon-hand" viewBox="0 0 40 40" fill="none" stroke="currentColor" stroke-width="1.4" stroke-linecap="round" stroke-linejoin="round">
      <path d="M9 30 C5 25 6 19 10 16 L18 8 C20 6 22 8 21 10 L17 15 L26 7 C28 5 30 7 28 9 L23 14 L29 10 C31 8 33 10 31 12 L25 17 L29 15 C31 14 32 16 30 18 L20 28 C17 31 12 32 9 30Z"/>
      <path d="M16 22 c-2 -2 1 -4 2 -2 c1 -2 4 0 2 2 l-2 2Z"/>
    </symbol>
    <symbol id="icon-no-preservatives" viewBox="0 0 40 40" fill="none" stroke="currentColor" stroke-width="1.4" stroke-linecap="round" stroke-linejoin="round">
      <circle cx="20" cy="20" r="18"/>
      <path d="M17 8 H23 M18 8 V17 L11 29 H29 L22 17 V8"/>
      <circle cx="17" cy="25" r="1.3"/><circle cx="22" cy="24" r="1"/>
      <path d="M8 33 L33 8"/>
    </symbol>
    <symbol id="icon-no-heat" viewBox="0 0 40 40" fill="none" stroke="currentColor" stroke-width="1.4" stroke-linecap="round" stroke-linejoin="round">
      <circle cx="20" cy="20" r="18"/>
      <path d="M18 8 a2 2 0 0 1 4 0 V24 a4.5 4.5 0 1 1 -4 0Z"/>
      <circle cx="20" cy="28" r="1.8"/>
      <path d="M23 12 H25 M23 16 H25 M23 20 H25 M8 33 L33 8"/>
    </symbol>
    <symbol id="icon-no-sugar" viewBox="0 0 40 40" fill="none" stroke="currentColor" stroke-width="1.4" stroke-linecap="round" stroke-linejoin="round">
      <circle cx="20" cy="20" r="18"/>
      <path d="M20 9 L25 11.5 V17 L20 19.5 L15 17 V11.5Z M15 11.5 L20 14 L25 11.5 M20 14 V19.5"/>
      <path d="M13 19 L18 21.5 V27 L13 29.5 L8 27 V21.5Z M8 21.5 L13 24 L18 21.5 M13 24 V29.5"/>
      <path d="M27 19 L32 21.5 V27 L27 29.5 L22 27 V21.5Z M22 21.5 L27 24 L32 21.5 M27 24 V29.5"/>
      <path d="M8 33 L33 8"/>
    </symbol>
  </defs>
</svg>

<main class="sheet">
  <section class="label label--light">
    <h1 class="brand-name">navisa</h1>
    <div class="divider"></div>
    <ul class="claims">
      <li class="claim"><svg><use href="#icon-fresh"/></svg>ULTRA-FRESH</li>
      <li class="claim"><svg><use href="#icon-hand"/></svg>ULTRA-FRESH</li>
      <li class="claim"><svg><use href="#icon-no-preservatives"/></svg>PRESERVATIVES<br>FREE</li>
      <li class="claim"><svg><use href="#icon-no-heat"/></svg>NO HEAT-<br>TREATED</li>
      <li class="claim"><svg><use href="#icon-no-sugar"/></svg>NO ADDED-<br>SUGAR</li>
    </ul>
    <h2 class="product-name">SELU VANE</h2>
    <p class="ingredients">Mango, Pineapple, Lemon<br>Passion Fruits, Orange</p>
    <div class="fruit-art" role="img" aria-label="Line illustration of a pineapple and a mango"></div>
    <p class="tagline">Premium crafted smoothies. A unique commitment to freshness.</p>
  </section>

  <section class="label label--dark">
    <h1 class="brand-name">navisa</h1>
    <div class="divider"></div>
    <ul class="claims">
      <li class="claim"><svg><use href="#icon-fresh"/></svg>ULTRA-FRESH</li>
      <li class="claim"><svg><use href="#icon-hand"/></svg>ULTRA-FRESH</li>
      <li class="claim"><svg><use href="#icon-no-preservatives"/></svg>PRESERVATIVES<br>FREE</li>
      <li class="claim"><svg><use href="#icon-no-heat"/></svg>NO HEAT-<br>TREATED</li>
      <li class="claim"><svg><use href="#icon-no-sugar"/></svg>NO ADDED-<br>SUGAR</li>
    </ul>
    <h2 class="product-name">SELU VANE</h2>
    <p class="ingredients">Mango, Pineapple, Lemon<br>Passion Fruits, Orange</p>
    <div class="fruit-art" role="img" aria-label="Line illustration of a pineapple and a mango"></div>
    <p class="tagline">Premium crafted smoothies. A unique commitment to freshness.</p>
  </section>

  <div class="smoothie-field" aria-hidden="true"></div>

  <section class="label label--clear">
    <h1 class="brand-name">navisa</h1>
    <div class="divider"></div>
    <ul class="claims">
      <li class="claim"><svg><use href="#icon-fresh"/></svg>ULTRA-FRESH</li>
      <li class="claim"><svg><use href="#icon-hand"/></svg>ULTRA-FRESH</li>
      <li class="claim"><svg><use href="#icon-no-preservatives"/></svg>PRESERVATIVES<br>FREE</li>
      <li class="claim"><svg><use href="#icon-no-heat"/></svg>NO HEAT-<br>TREATED</li>
      <li class="claim"><svg><use href="#icon-no-sugar"/></svg>NO ADDED-<br>SUGAR</li>
    </ul>
    <h2 class="product-name">SELU VANE</h2>
    <p class="ingredients">Mango, Pineapple, Lemon<br>Passion Fruits, Orange</p>
    <div class="fruit-art" role="img" aria-label="Line illustration of a pineapple and a mango"></div>
    <p class="tagline">Premium crafted smoothies. A unique commitment to freshness.</p>
  </section>
</main>
</body>
</html>
```